Buch-/eBook-Cover für ein Fantasy Roman
Zielgruppe
Meine Zielgruppe sind Jugendliche und junge Erwachsene, aber auch für Ältere könnte mein Buch interessant sein.
Aufgabenstellung
Bei meinem Buch handelt es sich um einen Fantasy Roman. Es heißt 'Nachtfalter - Wahrheit braucht ihre Zeit' und der Autor ist Mara Oswaldtinger.
Das Buch handelt von einem Mädchen, welches eigentlich ein ganz normales Leben führt, aber dieses durch eine Pressekonferenz vom Präsidenten komplett durcheinander gerät. Denn viele Menschen sollen an einem Virus leiden. Die Menschen sollen sich aber keine Sorgen machen. Doch alles läuft durcheinander, da die infizierten Menschen einer nach dem anderen spurlos verschwinden.
Auf meinem Cover soll keine Figur zu sehen sein. Ich hätte gerne ein Zusammenspiel zwischen den Farben Blau und Grün. sie sollen harmonisch und fließend ineinander übergehen. Auch etwas Glitzer für etwas Geheimnisvolles darf auf dem Cover sein. Den Titel hätte ich gerne in der Mitte. Wo der Autorname stehen soll, bin ich offen.

```html
<!DOCTYPE html>
<html lang="de">
<head>
<meta charset="utf-8">
<title>Nachtfalter – Buchcover</title>
<link rel="stylesheet" href="https://fonts.googleapis.com/css2?family=Lato:wght@400&family=Playfair+Display+SC:wght@700&family=Yellowtail&display=swap">
<style>
  :root {
    --stage: #e2e2e2;
    --deep: #12303a;
    --teal: #1d5f66;
    --sea: #2a7c78;
    --glow: #8fa77a;
    --ink: #ffffff;
  }
  html, body {
    margin: 0;
    padding: 0;
    width: 1200px;
    height: 857px;
    overflow: hidden;
    background: var(--stage);
  }
  .canvas {
    position: relative;
    width: 1200px;
    height: 857px;
  }
  .cover {
    position: absolute;
    left: 333px;
    top: 29px;
    width: 535px;
    height: 799px;
    overflow: hidden;
    box-shadow: 6px 6px 8px rgba(0,0,0,0.28);
  }
  .cover-art {
    position: absolute;
    inset: 0;
    background:
      radial-gradient(ellipse 40% 22% at 58% 6%, rgba(143,167,122,0.75), transparent 70%),
      radial-gradient(ellipse 60% 30% at 40% 35%, rgba(42,124,120,0.8), transparent 75%),
      radial-gradient(ellipse 50% 35% at 70% 60%, rgba(35,110,110,0.7), transparent 75%),
      linear-gradient(165deg, var(--sea) 0%, var(--teal) 40%, #1a5258 65%, var(--deep) 100%);
  }
  .author {
    position: absolute;
    top: 96px;
    width: 100%;
    margin: 0;
    text-align: center;
    font-family: "Lato", sans-serif;
    font-weight: 400;
    font-size: 27px;
    letter-spacing: 0.07em;
    color: var(--ink);
    text-transform: uppercase;
  }
  .title {
    position: absolute;
    top: 200px;
    width: 100%;
    margin: 0;
    text-align: center;
    font-family: "Playfair Display SC", serif;
    font-weight: 700;
    font-size: 54px;
    line-height: 1;
    color: var(--ink);
    white-space: nowrap;
  }
  .title-initial {
    font-size: 2.2em;
    vertical-align: -0.03em;
  }
  .subtitle {
    position: absolute;
    top: 362px;
    width: 100%;
    margin: 0;
    text-align: center;
    font-family: "Yellowtail", cursive;
    font-size: 74px;
    line-height: 78px;
    color: var(--ink);
  }
  .subtitle span { display: block; }
</style>
</head>
<body>
  <main class="canvas">
    <section class="cover">
      <div class="cover-art" role="img" aria-label="Abstrakte, fließende Wellen in Blau- und Grüntönen mit goldenen Linien und Glitzerpunkten"></div>
      <p class="author">Mara Oswaldtinger</p>
      <h1 class="title"><span class="title-initial">N</span>achtfalter</h1>
      <h2 class="subtitle">
        <span>Wahrheit</span>
        <span>braucht</span>
        <span>ihre</span>
        <span>Zeit</span>
      </h2>
    </section>
  </main>
</body>
</html>
```